Business Card Design Project

I need a business card design for an Organic drive thru coffee kiosk. We will serve organic coffee, teas & smoothies and will serve healthy breakfast food/snacks for people on the go.
I want the card to have 2-3 colors max (earthy colors like browns, greens and so on).
I have attached the logo I want used and would love to play off the theme of "balance."
Include:
Tidy-Kettle Coffee
address: 4820 Gorvin Ct. Raleigh, NC 27583
phone: 919-731-4062
website: www.tidy-kettle.com (website is not up yet but still include it on card)
email: Rosalind@tidy-kettle.com
I want one of the following sayings somewhere on the card (the front or back is fine):
"Sip & Snack Tidy, on the go!"
"Break the fast with Tidy-Kettle"
Maybe on the back list what we offer:
-Organic coffee, espresso & tea
-Blendora smoothies & protein shakes
-Zesty Pour (100% fresh local fruit and veggies)
-Tender Nibs

```html
<!DOCTYPE html>
<html lang="en">
<head>
<meta charset="utf-8">
<title>Tidy-Kettle Business Card</title>
<link rel="stylesheet" href="https://fonts.googleapis.com/css2?family=Strait&family=Josefin+Sans:wght@400;600&family=Open+Sans:wght@600&family=Arimo&display=swap">
<style>
  :root {
    --page: #f3f1ee;
    --card-light: #ebe8e5;
    --doodle-tone: #d9d3cd;
    --espresso: #3b2419;
    --bark: #4e3629;
    --bark-light: #5e4334;
    --rust: #8c4a33;
    --rust-soft: #a8654a;
    --cream: #f2ebe3;
  }
  * { box-sizing: border-box; margin: 0; padding: 0; }
  html, body {
    width: 1200px; height: 1000px; overflow: hidden;
    background: var(--page);
  }
  .card-set {
    position: absolute; top: 350px; left: 60px;
    display: flex; gap: 60px;
  }
  .card {
    position: relative; width: 520px; height: 300px;
    overflow: hidden;
    box-shadow: 0 14px 22px rgba(0,0,0,0.12);
  }
  .card--front { background: var(--card-light); }
  .card--back { background: linear-gradient(90deg, var(--bark) 0%, var(--bark-light) 100%); }

  .sketch-field {
    position: absolute; inset: 0 0 110px 0;
    background: radial-gradient(ellipse at 50% 45%, var(--card-light) 30%, var(--doodle-tone) 100%);
    opacity: .8;
  }
  .brand {
    position: absolute; left: 0; right: 0;
    display: flex; flex-direction: column; align-items: center;
  }
  .card--front .brand { top: 32px; }
  .card--back .brand { top: 50px; }
  .brand__dot {
    width: 36px; height: 36px; border-radius: 50%;
    background: var(--rust); margin-bottom: 8px;
  }
  .card--back .brand__dot { width: 30px; height: 30px; }
  .brand__name {
    font-family: "Strait", sans-serif;
    font-size: 54px; line-height: 1; color: var(--espresso);
  }
  .card--back .brand__name { font-size: 46px; color: var(--cream); }
  .brand__tagline {
    font-family: "Josefin Sans", sans-serif; font-weight: 600;
    font-size: 11px; letter-spacing: 3px; color: var(--rust);
    margin-top: 6px;
  }
  .card--back .brand__tagline { font-size: 10px; color: var(--rust-soft); }

  .swoosh { position: absolute; inset: 0; }
  .slogan {
    position: absolute; left: 0; right: 0; top: 207px;
    text-align: center;
    font-family: "Open Sans", sans-serif; font-weight: 600;
    font-size: 19px; color: var(--cream);
    transform: rotate(1deg);
  }
  .contact {
    position: absolute; left: 0; right: 0; top: 212px;
    text-align: center;
    font-family: "Arimo", sans-serif; font-size: 10.5px;
    line-height: 1.6; color: var(--cream);
  }
</style>
</head>
<body>
<main class="card-set">
  <section class="card card--front">
    <div class="sketch-field" role="img" aria-label="Light hand-drawn sketches of coffee cups, a tea mug, a leaf, a carrot, an iced drink and the word coffee"></div>
    <div class="brand">
      <span class="brand__dot"></span>
      <span class="brand__name">Tidy-Kettle</span>
      <span class="brand__tagline">ORGANIC COFFEE + CAFE</span>
    </div>
    <svg class="swoosh" viewBox="0 0 520 300" aria-hidden="true">
      <path d="M0 188 Q260 160 520 196" fill="none" stroke="#5a3a2b" stroke-width="1.5"/>
      <path d="M0 196 Q260 168 520 204 L520 250 Q260 222 0 244 Z" fill="#3b2419"/>
    </svg>
    <p class="slogan">Sip &amp; Snack Tidy, on the go!</p>
  </section>

  <section class="card card--back">
    <div class="brand">
      <span class="brand__dot"></span>
      <span class="brand__name">Tidy-Kettle</span>
      <span class="brand__tagline">ORGANIC COFFEE + CAFE</span>
    </div>
    <div class="contact">
      <p>visit: 4820 Gorvin Ct. Raleigh, NC 27583 - call: 919-731-4062</p>
      <p>write: rosalind@tidy-kettle.com - www.tidy-kettle.com</p>
    </div>
  </section>
</main>
</body>
</html>
```